Brume d'Orvelle Hand Crafted Candles promotional flyer

Hand Crafted Soy Candles - I need a flyer to promote my candles and to give information on care of candles.I want this to use the design and colours I already have for my labels and the photo I have attached.I am aiming at a sophisticated market so would like to reflect this in the design.
Should appeal to sophisticated women who enjoy the pleasure of candles - to enhance their enjoyment of life - gives them the 'brume d'orvelle'.
the candles are hand crafted from all natural ingredients, environmentally friendly and with exquisite fragrances

Target Market(s)

sophisticated females

Industry/Entity Type

Promotional

Font styles to use
Script

Colors
cfeae6
ecdaeb

Requirements
Must have
• something expressing 'brume d'orvelle' - the enjoyment of candles
Should not have
• bright colours

```html
<!DOCTYPE html>
<html lang="en">
<head>
<meta charset="utf-8">
<title>Brume d'Orvelle Hand Crafted Candles – Flyer</title>
<link href="https://fonts.googleapis.com/css2?family=Pinyon+Script&family=Cormorant+SC:wght@600&family=Didact+Gothic&family=Mulish:ital,wght@0,700;1,800&family=Titillium+Web:wght@700&display=swap" rel="stylesheet">
<style>
:root{
  --page-bg:#dcd8d4;
  --night-deep:#150f28;
  --night-mid:#2e2350;
  --night-glow:#4a3a78;
  --mint:#cfeae6;
  --mint-light:#e2f4f1;
  --lilac:#ecdaeb;
  --gold:#d9a834;
  --gold-light:#f3d57a;
  --maroon:#8e3535;
  --ink:#2c2430;
  --rule:#9b8f96;
  --white:#ffffff;
}
*{box-sizing:border-box;margin:0;padding:0}
html,body{width:1200px;height:1200px;overflow:hidden}
body{background:var(--page-bg);position:relative;font-family:"Didact Gothic",sans-serif;color:var(--ink)}
.flyer{position:absolute;left:196px;top:30px;width:807px;height:1140px;overflow:hidden;
  background:linear-gradient(180deg,var(--mint) 0%,var(--mint-light) 55%,var(--mint) 100%);
  box-shadow:0 6px 24px rgba(0,0,0,.25)}
.hero-band{position:absolute;left:0;top:0;width:807px;height:470px}
.brand-seal{position:absolute;left:168px;top:25px;width:228px;height:228px;border-radius:50%;
  background:radial-gradient(circle,var(--white) 0%,#dff0ef 100%);
  display:flex;flex-direction:column;align-items:center;justify-content:center;text-align:center;gap:8px}
.brand-seal .brand-name{font-family:"Cormorant SC",serif;font-weight:600;font-size:26px;color:var(--night-mid);line-height:1}
.brand-seal .brand-sub{font-family:"Cormorant SC",serif;font-weight:600;font-size:13px;color:var(--night-mid);line-height:1}
.product-photo{position:absolute;left:36px;top:260px;width:436px;height:158px;border-radius:6px;
  background:linear-gradient(90deg,#1b1a22 0%,#d8d7b2 35%,#ece9b8 62%,#2c3e8c 88%,transparent 100%)}
.model-photo{position:absolute;left:492px;top:30px;width:315px;height:379px;
  background:radial-gradient(ellipse at 50% 72%,#f4c58a 0%,#a48cb0 28%,#5a4b7c 60%,transparent 85%)}

.title-script{position:absolute;left:40px;top:460px;font-family:"Pinyon Script",cursive;font-weight:400;font-size:46px;color:var(--night-deep);line-height:1;white-space:nowrap}
.title-sub{position:absolute;left:150px;width:235px;top:515px;font-family:"Cormorant SC",serif;font-weight:600;font-size:15px;letter-spacing:.3px;color:var(--night-deep);text-align:right;white-space:nowrap;line-height:18px}
.title-rule{position:absolute;left:40px;top:536px;width:384px;height:1px;background:var(--rule)}

.bullets{position:absolute;left:40px;list-style:none;width:372px}
.bullets li{position:relative;padding-left:12px;font-size:13px;line-height:16px;margin-bottom:4px}
.bullets li::before{content:"";position:absolute;left:0;top:6px;width:6px;height:6px;border-radius:50%;background:var(--maroon)}
.bullets.intro{top:545px}
.bullets.intro li{max-width:340px}
.bullets.intro li.beside-jar{max-width:250px}
.bullets.soy{top:760px}
.bullets.refill{top:952px}
.bullets.refill li{margin-bottom:11px}
.section-head{position:absolute;left:54px;font-family:"Mulish",sans-serif;font-weight:700;font-size:18px;line-height:22px;color:var(--maroon)}
.section-head.soy-head{top:730px}
.section-head.refill-head{top:921px}
.jar-photo{position:absolute;left:296px;top:605px;width:116px;height:146px;border-radius:8px 8px 22px 22px;
  background:radial-gradient(ellipse at 55% 45%,#dfe9ec 0%,#7d8c98 38%,#101216 70%)}

.divider{position:absolute;left:424px;top:488px;width:1px;height:578px;background:var(--rule)}
.care-head{position:absolute;left:457px;top:482px;width:320px;font-family:"Mulish",sans-serif;font-style:italic;font-weight:800;font-size:13px;line-height:16.5px;color:var(--maroon)}
.care-item{position:absolute;left:435px;width:345px;padding-left:24px;font-size:12px;line-height:14.6px}
.care-num{position:absolute;left:0;top:-1px;width:18px;height:18px;border-radius:50%;background:var(--maroon);color:var(--white);font-family:"Mulish",sans-serif;font-weight:700;font-size:11px;line-height:18px;text-align:center}

.footer{position:absolute;left:0;top:1076px;width:807px;height:64px;background:linear-gradient(180deg,var(--night-mid),var(--night-deep));border-top:3px solid var(--gold)}
.footer-phone{position:absolute;left:89px;top:12px;display:flex;align-items:center;gap:8px;font-family:"Titillium Web",sans-serif;font-weight:700;font-size:27px;line-height:34px;color:var(--white);letter-spacing:.5px}
.footer-contacts{position:absolute;left:486px;top:6px;font-family:"Titillium Web",sans-serif;font-weight:700;font-size:14.5px;color:var(--white);line-height:23px}
.footer-contacts div{display:flex;align-items:center;gap:8px}
</style>
</head>
<body>
<main class="flyer">
  <svg class="hero-band" viewBox="0 0 807 470" aria-hidden="true">
    <defs>
      <radialGradient id="nightSky" cx="55%" cy="40%" r="75%">
        <stop offset="0" stop-color="#4a3a78"/>
        <stop offset=".6" stop-color="#2e2350"/>
        <stop offset="1" stop-color="#150f28"/>
      </radialGradient>
      <linearGradient id="goldEdge" x1="0" x2="1">
        <stop offset="0" stop-color="#d9a834"/>
        <stop offset=".5" stop-color="#f3d57a"/>
        <stop offset="1" stop-color="#d9a834"/>
      </linearGradient>
    </defs>
    <path d="M0,0 H807 V414 Q403,500 0,414 Z" fill="url(#nightSky)"/>
    <path d="M0,416 Q403,502 807,416" fill="none" stroke="url(#goldEdge)" stroke-width="5"/>
    <path d="M0,424 Q403,508 807,424" fill="none" stroke="#ffffff" stroke-opacity=".6" stroke-width="1.5"/>
  </svg>

  <div class="brand-seal"><span class="brand-name">Brume d'Orvelle</span><span class="brand-sub">Handcrafted Soy Candles</span></div>
  <div class="product-photo" role="img" aria-label="Row of four labelled soy candle jars in black, cream, glass and blue"></div>
  <div class="model-photo" role="img" aria-label="Woman with eyes closed holding a glowing candle in cupped hands"></div>

  <h1 class="title-script">Brume d'Orvelle</h1>
  <p class="title-sub">Handcrafted Soy Candled</p>
  <div class="title-rule"></div>

  <ul class="bullets intro">
    <li>Brume d'Orvelle – an exuberant enjoyment of life – these candles will fill you with “Brume d'Orvelle”.</li>
    <li>Candles are lovingly hand-poured and use only the finest of ingredients and fragrances</li>
    <li class="beside-jar">Hand crafted soy candle creations</li>
    <li class="beside-jar">Completely non-toxic</li>
    <li class="beside-jar">Exquisite fragrances</li>
    <li class="beside-jar">Clean burning</li>
    <li class="beside-jar">Environmentally friendly.</li>
  </ul>
  <div class="jar-photo" role="img" aria-label="Black glass candle jar with round label"></div>

  <h2 class="section-head soy-head">Why soy wax?</h2>
  <ul class="bullets soy">
    <li>Soft smooth wax that burns clear – no soot or smoke</li>
    <li>Soy wax candles burn up to 50% longer than traditional paraffin candles</li>
    <li>Made form soya beans, a renewable natural resource that supports and sustains agriculture – it is biodegradable and environmentally friendly.</li>
    <li>Soy wax burns cooler than paraffin and disperse the fragrance more fully.</li>
  </ul>

  <h2 class="section-head refill-head">Containers can be refilled</h2>
  <ul class="bullets refill">
    <li>I offer a refill service -if you return you containers to me I can refill with the fragrance of your choice</li>
    <li>Or if you have a special container you would like to use for your candle just contact me for a quote.</li>
    <li>I have a wide range of fragrances - please contact me for details.</li>
  </ul>

  <div class="divider"></div>

  <h2 class="care-head">How to care for your candle – the following tips will ensure you have a long lasting, fully fragranced candle</h2>
  <div class="care-item" style="top:543px"><span class="care-num">1.</span><p>When lighting you candle for the first time, allow the wax to melt all the way to the sides of the container – this creates a ‘memory’ and avoids ‘tunnelling’ as the candle burns.</p></div>
  <div class="care-item" style="top:615px"><span class="care-num">2.</span><p>Always trim the wick to about 6-8mm before re-lighting your candle. This will ensure a long lasting candle, minimise soot and remove any mushrooming of the wick from a previous burn.</p></div>
  <div class="care-item" style="top:689px"><span class="care-num">3.</span><p>It is preferable to use a candle ‘snuffer’ to extinguish the flame, or a lid if the candle has one. Alternatively, you can dip the wick into the melted wax and then straightening. This wil stop the wick from smoking and help with relighting.</p></div>
  <div class="care-item" style="top:777px"><span class="care-num">4.</span><p>All Brume d'Orvelle candles are hand poured not massed produced – although every effort is made to ensure consistency, every candle may be different.</p></div>
  <div class="care-item" style="top:835px"><span class="care-num">5.</span><p>Sometimes you may notice darker patches or wet spots - this is not a fault it is just the natural way the wax has set – it does not affect the candle in anyway.</p></div>
  <div class="care-item" style="top:893px"><span class="care-num">6.</span><p>The top of the candle may also appear slightly uneven – this is just a sign of natural soy wax being hand poured.</p></div>
  <div class="care-item" style="top:951px"><span class="care-num">7.</span><p>Do not leave your candle in the sunlight as it may turn a yellow colour – again this does not affect the candle in anyway – it just loses its creamy white colour.</p></div>
  <div class="care-item" style="top:1025px"><span class="care-num">8.</span><p>As these candles contain no preservatives or chemicals it is recommended that they should be used within 6 months.</p></div>

  <footer class="footer">
    <div class="footer-phone">
      <svg width="22" height="22" viewBox="0 0 24 24" aria-hidden="true"><path d="M6.6 10.8a15 15 0 0 0 6.6 6.6l2.2-2.2a1 1 0 0 1 1-.25 11.4 11.4 0 0 0 3.6.57 1 1 0 0 1 1 1V20a1 1 0 0 1-1 1A17 17 0 0 1 3 4a1 1 0 0 1 1-1h3.5a1 1 0 0 1 1 1c0 1.25.2 2.45.57 3.6a1 1 0 0 1-.25 1z" fill="#fff"/></svg>
      <span>021 555 0187</span>
    </div>
    <div class="footer-contacts">
      <div><svg width="18" height="13" viewBox="0 0 18 13" aria-hidden="true"><rect x=".5" y=".5" width="17" height="12" fill="#fff"/><path d="M.5 .5 9 7.5 17.5 .5" fill="none" stroke="#2e2350" stroke-width="1.4"/></svg><span>claire.hollis@mailbox.co.nz</span></div>
      <div><svg width="18" height="18" viewBox="0 0 18 18" aria-hidden="true"><circle cx="9" cy="9" r="7.5" fill="none" stroke="#fff" stroke-width="1.6"/><path d="M1.5 9h15M9 1.5c3 3.5 3 11.5 0 15M9 1.5c-3 3.5-3 11.5 0 15" fill="none" stroke="#fff" stroke-width="1.3"/></svg><span>www.brumedorvelle.co.nz</span></div>
    </div>
  </footer>
</main>
</body>
</html>
```